Business Card design for a company called Copper Vale HQ

I need a business card design for my oil fired boiler servicing company. I have a logo design already and Im just looking that incorporated into the business card design. card details; Copper Vale HQ
Oil Burner Servicing - Mid Ulster Area
Service Engineer - Dean Morrow
Mobile 07700900418
email - Copper.Vale.HQ@brandmail.test
www.coppervalehq.test
I carry out Servicing, Commissioning, Fault Finding, Warranty Validation
Target Market(s)
home owners with oil fired central heating
Industry/Entity Type
Business
Contact Information for Business Card
Copper Vale HQ
Tell. 07700900418
Web: www.coppervalehq.test
email Copper.Vale.HQ@Brandmail.Test
Servicing Fault Finding Commissioning Warranty Validation
Look and feel

```html
<!DOCTYPE html>
<html lang="en">
<head>
<meta charset="utf-8">
<title>Copper Vale HQ – Business Card</title>
<link rel="stylesheet" href="https://fonts.googleapis.com/css2?family=Open+Sans:wght@400;600&family=Lustria&display=swap">
<style>
  :root {
    --canvas-bg: #e9e9e7;
    --card-bg: #ffffff;
    --brand-green: #6cc04a;
    --brand-green-light: #8fd16a;
    --ink: #1c1c1c;
    --rule: #2a2a2a;
  }
  * { margin: 0; padding: 0; box-sizing: border-box; }
  html, body {
    width: 1200px; height: 892px; overflow: hidden;
    background: var(--canvas-bg);
  }
  .card {
    position: absolute; left: 100px; top: 160px;
    width: 1000px; height: 571px;
    background: var(--card-bg);
    border-radius: 26px;
    box-shadow: 0 6px 24px rgba(0,0,0,0.12);
    font-family: "Open Sans", sans-serif;
    color: var(--ink);
  }
  .brand { position: absolute; left: 60px; top: 62px; display: flex; align-items: center; gap: 22px; }
  .brand-dot { width: 104px; height: 104px; border-radius: 50%; background: var(--brand-green); flex: none; }
  .brand-name {
    font-family: "Open Sans", sans-serif; font-weight: 600;
    font-size: 74px; line-height: 1; color: var(--brand-green); letter-spacing: -1px;
  }
  .brand-tagline {
    position: absolute; left: 188px; top: 160px;
    font-size: 15px; letter-spacing: 3.2px; text-transform: uppercase;
    color: var(--brand-green-light);
  }
  .divider { position: absolute; left: 60px; top: 312px; width: 582px; height: 2px; background: var(--rule); }
  .engineer { position: absolute; left: 652px; top: 226px; }
  .engineer-name { font-family: "Lustria", serif; font-size: 46px; color: var(--brand-green); line-height: 1.1; }
  .engineer-role { font-family: "Lustria", serif; font-size: 28px; color: var(--ink); margin-top: 4px; }
  .contacts { position: absolute; left: 60px; top: 352px; list-style: none; }
  .contact { display: flex; align-items: center; gap: 16px; height: 44px; font-size: 25px; }
  .contact-icon { width: 20px; height: 20px; flex: none; }
  .services { position: absolute; left: 96px; top: 490px; font-size: 27px; }
</style>
</head>
<body>
  <div class="card">
    <div class="brand">
      <span class="brand-dot"></span>
      <span class="brand-name">Copper Vale HQ</span>
    </div>
    <div class="brand-tagline">Oil Burner Servicing - Mid Ulster Area</div>

    <div class="divider"></div>
    <div class="engineer">
      <div class="engineer-name">Dean Morrow</div>
      <div class="engineer-role">Service Engineer</div>
    </div>

    <ul class="contacts">
      <li class="contact">
        <svg class="contact-icon" viewBox="0 0 20 20"><rect width="20" height="20" rx="2" fill="var(--brand-green)"/><path d="M6 4.5c1 0 1.6 2.4 1 3l-.8.7c.6 1.6 2 3 3.6 3.6l.7-.8c.6-.6 3 0 3 1 0 1.2-1 2.5-2.3 2.3C7.6 13.8 5.7 11.9 5.2 8 5 6.3 5.2 4.5 6 4.5z" fill="#fff"/></svg>
        <span>07700900418</span>
      </li>
      <li class="contact">
        <svg class="contact-icon" viewBox="0 0 20 20"><rect width="20" height="20" rx="2" fill="var(--brand-green)"/><rect x="4" y="6" width="12" height="8" fill="none" stroke="#fff" stroke-width="1.4"/><path d="M4 6l6 5 6-5" fill="none" stroke="#fff" stroke-width="1.4"/></svg>
        <span>Copper.Vale.HQ@Brandmail.Test</span>
      </li>
      <li class="contact">
        <svg class="contact-icon" viewBox="0 0 20 20"><rect width="20" height="20" rx="2" fill="var(--brand-green)"/><circle cx="10" cy="10" r="5.5" fill="none" stroke="#fff" stroke-width="1.4"/><path d="M4.5 10h11M10 4.5c-2.5 3-2.5 8 0 11M10 4.5c2.5 3 2.5 8 0 11" fill="none" stroke="#fff" stroke-width="1.1"/></svg>
        <span>www.coppervalehq.test</span>
      </li>
    </ul>
    <div class="services">Servicing Fault Finding Commissioning Warranty Validation</div>
  </div>
</body>
</html>
```